Building company business card

Design and print business cards for BRENTHOLM PTY LTD.
A residantial homes building company.
Mark Lantern already designed the company Logo.

```html
<!DOCTYPE html>
<html lang="en">
<head>
<meta charset="utf-8">
<title>BRENTHOLM PTY LTD – Business Card</title>
<link href="https://fonts.googleapis.com/css2?family=Arimo:wght@400;700&display=swap" rel="stylesheet">
<style>
  :root {
    --navy: #23296b;
    --gold: #c9983a;
    --gold-light: #e6c164;
    --paper: #ffffff;
    --backdrop: #d9d8d4;
    --ink: #1f1f24;
  }
  * { box-sizing: border-box; margin: 0; padding: 0; }
  html, body {
    width: 1200px;
    height: 801px;
    overflow: hidden;
  }
  body {
    background: var(--backdrop);
    font-family: "Arimo", Arial, sans-serif;
    color: var(--ink);
    position: relative;
  }
  .card {
    position: absolute;
    top: 235px;
    width: 540px;
    height: 330px;
    background: var(--paper);
    border-radius: 16px;
    border-bottom: 3px solid var(--navy);
    border-left: 1px solid var(--navy);
    overflow: hidden;
  }
  .card--front { left: 40px; }
  .card--back { left: 620px; }

  /* Front */
  .accent-bar {
    position: absolute;
    top: 0;
    right: 40px;
    width: 28px;
    height: 14px;
    background: var(--navy);
  }
  .holder {
    position: absolute;
    top: 30px;
    right: 40px;
    text-align: right;
    color: var(--navy);
  }
  .holder__name {
    font-weight: 700;
    font-size: 22px;
    letter-spacing: 0.3px;
  }
  .holder__role {
    font-size: 12px;
    color: var(--ink);
    margin-top: 2px;
  }
  .holder__company {
    font-weight: 700;
    font-size: 19px;
    margin-top: 22px;
    letter-spacing: 0.3px;
  }
  .brand {
    display: flex;
    align-items: center;
    gap: 8px;
    color: var(--navy);
    font-weight: 700;
  }
  .brand__mark {
    background: var(--gold);
    flex: none;
  }
  .card--front .brand {
    position: absolute;
    left: 30px;
    top: 138px;
    font-size: 22px;
  }
  .card--front .brand__mark { width: 14px; height: 14px; }
  .details {
    position: absolute;
    left: 30px;
    top: 180px;
    font-size: 13px;
    line-height: 17px;
    color: var(--ink);
  }
  .details__group + .details__group { margin-top: 8px; }
  .details__line {
    display: flex;
    align-items: center;
    gap: 7px;
  }
  .details__icon { width: 12px; height: 12px; flex: none; }

  /* Back */
  .card--back .brand {
    position: absolute;
    left: 0;
    right: 0;
    top: 0;
    bottom: 0;
    justify-content: center;
    font-size: 50px;
    gap: 14px;
  }
  .card--back .brand__mark { width: 30px; height: 30px; }
</style>
</head>
<body>

  <section class="card card--front" aria-label="Business card front">
    <span class="accent-bar"></span>
    <div class="holder">
      <p class="holder__name">CASPAR (Cass) HOLLIS</p>
      <p class="holder__role">Director</p>
      <p class="holder__company">BRENTHOLM PTY LTD</p>
    </div>

    <div class="brand">
      <span class="brand__mark"></span>
      <span class="brand__name">BRENTHOLM</span>
    </div>

    <div class="details">
      <div class="details__group">
        <p>ABN- 48 210 905 377</p>
        <p>CDB-U 51846</p>
      </div>
      <div class="details__group">
        <p>PO Box 482</p>
        <p>Fernleigh East Vic 3921</p>
      </div>
      <div class="details__group">
        <p class="details__line">
          <svg class="details__icon" viewBox="0 0 12 12" aria-hidden="true">
            <rect x="3" y="0.8" width="6" height="10.4" rx="1.2" fill="none" stroke="var(--navy)" stroke-width="1.4"/>
            <line x1="5" y1="9.2" x2="7" y2="9.2" stroke="var(--navy)" stroke-width="1"/>
          </svg>
          0400 555 218 &amp; 0400 555 634
        </p>
        <p class="details__line">
          <svg class="details__icon" viewBox="0 0 12 12" aria-hidden="true">
            <rect x="0.5" y="2.5" width="11" height="7.5" fill="var(--navy)"/>
            <polyline points="0.8,2.8 6,6.8 11.2,2.8" fill="none" stroke="#fff" stroke-width="1"/>
          </svg>
          chh@brentholm-pl.co
        </p>
      </div>
    </div>
  </section>

  <section class="card card--back" aria-label="Business card back">
    <div class="brand">
      <span class="brand__mark"></span>
      <span class="brand__name">BRENTHOLM</span>
    </div>
  </section>

</body>
</html>
```